Marrowby's Vacation Rentals Business Card

Multi Million dollar villa rentals in the Dominican Republic.

Industry/Entity Type

Business

Contact Information for Business Card

I am looking for a high-end look around my company name/logo (see attached) on one side incorporating the following info: first and last name, title, address, phone #, email and company website. On the backside I want to add a full color picture of one of our villas (see attached).

```html
<!DOCTYPE html>
<html lang="en">
<head>
<meta charset="utf-8">
<title>Marrowby's Vacation Rentals – Business Card</title>
<link href="https://fonts.googleapis.com/css2?family=Open+Sans:wght@400;600&display=swap" rel="stylesheet">
<style>
  :root {
    --backdrop: #c9c9c9;
    --card: #f1f1ef;
    --orange: #e67e22;
    --orange-deep: #e2571f;
    --ink: #3a3a3a;
    --ink-soft: #555555;
  }
  * { box-sizing: border-box; margin: 0; padding: 0; }
  html, body {
    width: 1200px; height: 1200px; overflow: hidden;
    background: var(--backdrop);
    font-family: "Open Sans", sans-serif;
  }
  .stage {
    width: 1200px; height: 1200px;
    display: flex; align-items: center; justify-content: center;
  }
  .business-card {
    position: relative;
    width: 1000px; height: 572px;
    background: var(--card);
    border-radius: 34px;
    overflow: hidden;
    box-shadow: 0 14px 30px rgba(0,0,0,.18);
  }
  .band { position: absolute; left: 0; right: 0; background: var(--orange); }
  .band--top { top: 0; height: 40px; }
  .band--bottom { bottom: 0; height: 48px; }

  .brand {
    position: absolute; left: 80px; top: 200px;
    display: flex; align-items: center; gap: 18px;
  }
  .brand__dot {
    width: 70px; height: 70px; border-radius: 50%;
    background: var(--orange); flex: none;
  }
  .brand__name {
    color: var(--orange-deep);
    font-weight: 600; font-size: 34px; line-height: 1.15;
  }
  .brand__name span { display: block; font-size: 20px; }

  .contact {
    position: absolute; left: 530px; top: 188px;
    width: 440px;
    color: var(--ink);
  }
  .contact__name {
    font-size: 24px; font-weight: 600; letter-spacing: .5px;
    margin-bottom: 12px;
  }
  .contact__list { list-style: none; font-size: 19px; line-height: 1.35; }
  .contact__list li { display: flex; align-items: center; gap: 12px; }
  .contact__list svg { width: 18px; height: 18px; flex: none; }
  .contact__address {
    margin-top: 12px; font-size: 18px; line-height: 1.35; color: var(--ink-soft);
  }
</style>
</head>
<body>
<main class="stage">
  <section class="business-card">
    <div class="band band--top"></div>

    <div class="brand">
      <div class="brand__dot"></div>
      <p class="brand__name">Marrowby's<span>Vacation Rentals</span></p>
    </div>

    <div class="contact">
      <h1 class="contact__name">DALE FENWICK - CEO</h1>
      <ul class="contact__list">
        <li>
          <svg viewBox="0 0 18 18" aria-hidden="true"><rect x="4" y="1" width="10" height="16" rx="2" fill="none" stroke="#e67e22" stroke-width="2"/><rect x="6" y="4" width="6" height="7" fill="#e67e22"/></svg>
          +00 55 555 5555
        </li>
        <li>
          <svg viewBox="0 0 18 18" aria-hidden="true"><rect x="1" y="4" width="16" height="11" fill="none" stroke="#e67e22" stroke-width="2"/><path d="M1 4l8 6 8-6" fill="none" stroke="#e67e22" stroke-width="2"/></svg>
          dfenwick@marrowbysvacations.com
        </li>
        <li>
          <svg viewBox="0 0 18 18" aria-hidden="true"><circle cx="9" cy="9" r="7.5" fill="none" stroke="#e67e22" stroke-width="1.8"/><ellipse cx="9" cy="9" rx="3.5" ry="7.5" fill="none" stroke="#e67e22" stroke-width="1.5"/><path d="M1.5 9h15" stroke="#e67e22" stroke-width="1.5"/></svg>
          www.marrowbysvacations.com
        </li>
      </ul>
      <p class="contact__address">#14, Palmera Bldg, Costa Serena<br>Calle Brisa Marina 9, Sector Arenal<br>Bahía Norte, Zona 10420.</p>
    </div>

    <div class="band band--bottom"></div>
  </section>
</main>
</body>
</html>
```